Tennis String Package

Need a design for a tennis string package.
Design to be 15 cm in length and width.
I would like to create a style like the one in the image.
Brand name VUMIK
Product name SANDPIPER
Front and back designs are required.

Colors
0054AA
0677BA
7BADD7
CADEEF
E8F1F8
A7469A
B969AE
D3A5CF
EDDBEB
F8F0F9
6B429C
8869AF
B7A5CE
E3DAEB
F3F0F8

```html
<!DOCTYPE html>
<html lang="en">
<head>
<meta charset="utf-8">
<title>VUMIK SANDPIPER – String Package</title>
<link rel="stylesheet" href="https://fonts.googleapis.com/css2?family=Jost:wght@300;400&display=swap">
<style>
  :root {
    --page: #ffffff;
    --card: #1b1f1f;
    --hanger: #b3b3b3;
    --ink: #ffffff;
  }
  html, body {
    margin: 0;
    padding: 0;
    width: 1200px;
    height: 1200px;
    overflow: hidden;
    background: var(--page);
  }
  .package {
    display: block;
    width: 1200px;
    height: 1200px;
  }
  .package__face { fill: var(--card); }
  .package__hanger { fill: var(--hanger); }
  .package__rule { stroke: var(--ink); stroke-width: 2; }
  .brand-name {
    font-family: "Jost", sans-serif;
    font-weight: 300;
    font-size: 76px;
    fill: var(--ink);
  }
  .product-name {
    font-family: "Jost", sans-serif;
    font-weight: 400;
    font-size: 28px;
    letter-spacing: 2.5px;
    fill: var(--ink);
  }
  .spec {
    font-family: "Jost", sans-serif;
    font-weight: 300;
    font-size: 23px;
    letter-spacing: 1.8px;
    fill: var(--ink);
  }
</style>
</head>
<body>
  <svg class="package" viewBox="0 0 1200 1200" xmlns="http://www.w3.org/2000/svg">
    <rect class="package__face" x="137" y="151" width="905" height="905"/>

    <g class="package__hanger">
      <rect x="484" y="206" width="210" height="28" rx="14"/>
      <circle cx="589" cy="206" r="16"/>
    </g>

    <text class="brand-name" x="236" y="571">VUMIK</text>
    <text class="product-name" x="934" y="561" text-anchor="end">SANDPIPER</text>

    <line class="package__rule" x1="237" y1="637" x2="304" y2="637"/>

    <g class="specs">
      <text class="spec" x="237" y="717">Multifilament</text>
      <text class="spec" x="237" y="751">1.20mm/2m</text>
      <text class="spec" x="237" y="784">18g/40ft</text>
    </g>
  </svg>
</body>
</html>
```